computer animated growing cannabis plant

For 1 of our layers on our website www.brindlewoodgrow.nl we want a computer animated cannabis seed (s) that you see growing into a female cannabis plant.

Grow from seed till plant. ( also made it so that when scaled it is visible on mobile, for responsive website)
It would be nice if it looked like a time lapse of a growing cannabis plant.

The:
Slider wide is 955 pixels
Slider height is 348 pixels

Half of the slider wide we want to use for the animation. Other half must be text. If you can also think about some good texts with it would be great. We are thinking of text like:
-strong root system
-Flowering after 1 week
-Full buds after 7 weeks

For the frames we are thinking of something like this:
growing period (18 hours of light/6 hours darkness):
day 3: seedling surfaces
example:
day 4: seedcap cracks open to show cotyledons (first two leaves once the seed has sprouted) example: http://www.velkorantplantvault.com/img/marijuana-germination.jpg
day 6: first true leaves appear example http://www.quistbaldergarden.nl/wp-content/uploads/2014/05/zaailing2-140x110.jpg
day 10: second internodes with leaves show

Flowering period (12 hours light/12 hours dark):
week 1 of flowering. not visible yet
week 3 of flowering: first signs of flowering
week 7 of flowering: buds are swelling
Also optional to add a growing root system to each frame.
We are thinking about a minimum of 5 frames.

The slider software used is http://trembuvix.com/layer-slider.html in joomla 3.
This is a html 5 slider system. This slider system accepts (e.g.) png files.

It's important the size of the slider is as small as possible for the page speed.

Artwork must be made in a vector file.

After artwork is approved it must be placed in the software for this we can agree on a new price. We will pay extra to apply it in the software. This is negotiable after wards.

Anything not clear in the brief let me know then I can improve it. thks.
Updates

Industry/Entity Type

Computer

Font styles to use
Sans Serif

Requirements
Should not have
• no flash!!

```html
<!DOCTYPE html>
<html lang="en">
<head>
<meta charset="utf-8">
<title>Grow Slider – Strong Root System</title>
<link rel="stylesheet" href="https://fonts.googleapis.com/css2?family=Roboto:wght@700;900&display=swap">
<style>
  :root {
    --canvas-w: 1200px;
    --canvas-h: 437px;
    --cream-light: #f1ece0;
    --cream: #d8cdb2;
    --sand: #b9ab86;
    --leaf-pale: #c3d68a;
    --leaf-light: #a9c15a;
    --leaf: #6f8f2e;
    --leaf-dark: #3f5a1c;
    --stem: #5d7f2a;
    --bubble-edge: #ffffff;
    --ink: #1b1b1b;
  }
  * { margin: 0; padding: 0; box-sizing: border-box; }
  html, body {
    width: var(--canvas-w);
    height: var(--canvas-h);
    overflow: hidden;
    background: #ffffff;
  }
  .slide {
    position: relative;
    width: var(--canvas-w);
    height: var(--canvas-h);
    overflow: hidden;
  }
  .slide__backdrop {
    position: absolute;
    inset: 0;
    background:
      linear-gradient(90deg, var(--sand) 0%, var(--cream) 16%, var(--cream-light) 32%, #d9d6b4 44%, var(--leaf) 70%, var(--leaf-dark) 100%);
  }
  .slide__plant-photo {
    position: absolute;
    left: 460px;
    top: 0;
    width: 740px;
    height: 437px;
    background:
      radial-gradient(ellipse 22% 30% at 42% 44%, var(--leaf-pale) 0%, rgba(195,214,138,0) 75%),
      radial-gradient(ellipse 18% 26% at 30% 32%, var(--leaf-light) 0%, rgba(169,193,90,0) 75%),
      linear-gradient(22deg, rgba(93,127,42,0) 38%, rgba(93,127,42,0.75) 50%, rgba(93,127,42,0) 62%),
      radial-gradient(ellipse 30% 55% at 95% 25%, var(--leaf-dark) 0%, rgba(63,90,28,0) 75%),
      radial-gradient(ellipse 40% 40% at 30% 90%, var(--leaf) 0%, rgba(111,143,46,0) 70%);
  }
  .slide__overlay {
    position: absolute;
    inset: 0;
    width: 100%;
    height: 100%;
  }
  .badge__disc {
    fill: url(#badgeFill);
    stroke: var(--bubble-edge);
    stroke-width: 3;
    filter: url(#badgeShadow);
  }
  .badge__text {
    font-family: "Roboto", Arial, sans-serif;
    font-weight: 700;
    fill: var(--ink);
    text-anchor: middle;
    paint-order: stroke;
    stroke: rgba(255,255,255,0.8);
    stroke-width: 3px;
  }
  .badge__text--lead { font-size: 31px; }
  .badge__text--small { font-size: 21px; }
  .badge__text--mid { font-size: 25px; }
  .badge__text--strong { font-size: 26px; font-weight: 900; }
  .badge__text--strong-lg { font-size: 28px; font-weight: 900; }
  .bokeh {
    fill: url(#bokehFill);
    stroke: rgba(255,255,255,0.55);
    stroke-width: 1.5;
  }
</style>
</head>
<body>
  <main class="slide">
    <div class="slide__backdrop"></div>
    <div class="slide__plant-photo" role="img" aria-label="Close-up photograph of a young female cannabis plant: a green stem running diagonally with its first white pistils and small leaves, shown as the growing plant animation"></div>

    <svg class="slide__overlay" viewBox="0 0 1200 437" xmlns="http://www.w3.org/2000/svg">
      <defs>
        <radialGradient id="badgeFill" cx="50%" cy="40%" r="60%">
          <stop offset="0%" stop-color="#ffffff" stop-opacity="0.9"/>
          <stop offset="70%" stop-color="#f4f1ea" stop-opacity="0.82"/>
          <stop offset="100%" stop-color="#ddd8cc" stop-opacity="0.78"/>
        </radialGradient>
        <radialGradient id="bokehFill" cx="50%" cy="40%" r="60%">
          <stop offset="0%" stop-color="#ffffff" stop-opacity="0.15"/>
          <stop offset="100%" stop-color="#ffffff" stop-opacity="0.4"/>
        </radialGradient>
        <filter id="badgeShadow" x="-20%" y="-20%" width="140%" height="140%">
          <feDropShadow dx="0" dy="2" stdDeviation="4" flood-color="#000" flood-opacity="0.3"/>
        </filter>
      </defs>

      <g class="bokeh-set">
        <circle class="bokeh" cx="1042" cy="95" r="41"/>
        <circle class="bokeh" cx="986" cy="323" r="23"/>
        <circle class="bokeh" cx="734" cy="363" r="30"/>
      </g>

      <g class="badge badge--roots">
        <circle class="badge__disc" cx="142" cy="152" r="102"/>
        <text class="badge__text badge__text--lead" x="142" y="108">Strong</text>
        <text class="badge__text badge__text--lead" x="142" y="150">Root</text>
        <text class="badge__text badge__text--lead" x="142" y="192">System</text>
      </g>

      <g class="badge badge--flowering">
        <circle class="badge__disc" cx="534" cy="119" r="90"/>
        <text class="badge__text badge__text--small" x="534" y="100">Flowering</text>
        <text class="badge__text badge__text--small" x="534" y="127">after</text>
        <text class="badge__text badge__text--strong" x="534" y="161">1 WEEK</text>
      </g>

      <g class="badge badge--buds">
        <circle class="badge__disc" cx="379" cy="305" r="107"/>
        <text class="badge__text badge__text--mid" x="379" y="279">Full buds</text>
        <text class="badge__text badge__text--mid" x="379" y="315">after</text>
        <text class="badge__text badge__text--strong-lg" x="379" y="352">7 WEEKS</text>
      </g>
    </svg>
  </main>
</body>
</html>
```